Regional beer Valmo-Bräu needs new labels for 33cl Beercans

We are looking for a creative and professional design for our 33cl beer can label. The can itself is all black, and the design should be mainly in yellow and black colors to stand out on the store shelf.
The size of the label should be 206 mm x 80 mm

*Details and requirements:*

1. brand identity and target group
- Our brand stands for handcrafted quality with a modern touch.
- The target group is young adults and beer connoisseurs who value unique taste and stylish design.

2. style and aesthetics:*
- The design should be modern and eye-catching, inspired by the labels of Kelpe Brauhaus Hamburg.
- We prefer a minimalist style with clean lines and contrasts.

3. typography:*
- Use modern, legible fonts.
- Use freely available fonts.
- The brand name and important information should be emphasized.

4. images and graphics
- The logo can be used in its entirety or in individual parts.
- Illustrations or icons that emphasize the uniqueness of our beer are welcome.

5 *Colors:*
- Main colors are yellow and black.
- Accents in other colors are possible, but should be used sparingly.

6th *Legal requirements:*
- The label must provide space for legal information such as alcohol content, origin and barcode.

7 *Technical details
- Final files should be in AI, afdesign or PDF format with a resolution of at least 300 dpi.
- The design should be created in CMYK color model.

8th *Inspiration and references:*
- Examples of labels that we like are those of Kelpe Brauhaus Hamburg. We like their clear structure and modern look.

9 *Additional information:*
- The bottling date is printed on the can or bottle afterwards.
- Special features of our beer, such as flavor or special ingredients, should be highlighted.

We look forward to your creative suggestions and hope that you will help us to design a label that perfectly represents our brand!

The target group is young adults and beer connoisseurs who value unique taste and stylish design.

Beverage

Designer to choose colors to be used in the design.

• The design should be modern and eye-catching but minimalist style with clean lines and contrasts. should include the writing valmo-bräu (attachment)

```html
<!DOCTYPE html>
<html lang="de">
<head>
<meta charset="utf-8">
<title>Valmo-Bräu Helles – 33cl Dosenetikett</title>
<link rel="stylesheet" href="https://fonts.googleapis.com/css2?family=Arimo:wght@700&family=Ultra&display=swap">
<style>
  :root {
    --backdrop: #d5d5d5;
    --label-yellow: #f3bb1c;
    --label-yellow-light: #f8cc3c;
    --ink-black: #1c1c1c;
    --badge-black: #262626;
    --brand-yellow: #f1b92a;
    --shadow-white: #ffffff;
    --info-white: #ffffff;
    --volume-grey: #3a3a3a;
  }
  * { margin: 0; padding: 0; box-sizing: border-box; }
  html, body {
    width: 1200px;
    height: 1200px;
    overflow: hidden;
    background: var(--backdrop);
  }
  .canvas {
    position: relative;
    width: 1200px;
    height: 1200px;
  }
  .can-label {
    position: absolute;
    left: 437px;
    top: 212px;
    width: 326px;
    height: 808px;
    background: linear-gradient(90deg, var(--label-yellow) 0%, var(--label-yellow-light) 45%, var(--label-yellow) 100%);
    overflow: hidden;
  }
  .grunge {
    position: absolute;
    display: block;
  }
  .grunge--top-right { right: 0; top: 0; width: 110px; height: 210px; }
  .grunge--left { left: 0; top: 620px; width: 40px; height: 150px; }
  .brand-badge {
    position: absolute;
    left: 50%;
    top: 147px;
    width: 262px;
    height: 262px;
    margin-left: -131px;
    border-radius: 50%;
    background: var(--badge-black);
    box-shadow: 0 0 0 4px var(--shadow-white);
    display: flex;
    align-items: center;
    justify-content: center;
  }
  .brand-name {
    font-family: "Arimo", Arial, sans-serif;
    font-weight: 700;
    font-size: 36px;
    color: var(--brand-yellow);
    letter-spacing: 0.5px;
  }
  .beer-style {
    position: absolute;
    left: 0;
    right: 0;
    top: 668px;
    top: 455px;
    text-align: center;
    font-family: "Ultra", Georgia, serif;
    font-size: 66px;
    letter-spacing: 1px;
    color: var(--ink-black);
    text-shadow: 4px 3px 0 var(--shadow-white);
  }
  .alcohol {
    position: absolute;
    left: 0;
    right: 0;
    top: 660px;
    text-align: center;
    font-family: "Arimo", Arial, sans-serif;
    font-weight: 700;
    font-size: 19px;
    color: var(--info-white);
  }
  .volume {
    position: absolute;
    left: 0;
    right: 0;
    top: 692px;
    text-align: center;
    font-family: "Arimo", Arial, sans-serif;
    font-weight: 700;
    font-size: 60px;
    color: var(--volume-grey);
  }
</style>
</head>
<body>
  <main class="canvas">
    <section class="can-label">
      <svg class="grunge grunge--top-right" viewBox="0 0 110 210" role="img" aria-label="Black grunge brush texture in the upper corner">
        <polygon points="40,0 110,0 110,210 95,170 70,110 55,60" fill="var(--ink-black)" opacity="0.55"/>
      </svg>
      <svg class="grunge grunge--left" viewBox="0 0 40 150" role="img" aria-label="Black grunge brush texture along the left edge">
        <polygon points="0,0 30,30 38,90 20,150 0,150" fill="var(--ink-black)" opacity="0.5"/>
      </svg>

      <div class="brand-badge">
        <span class="brand-name">Valmo-Bräu</span>
      </div>

      <h1 class="beer-style">HELLES</h1>

      <p class="alcohol">Alc. 4.8% vol.</p>
      <p class="volume">33cl</p>
    </section>
  </main>
</body>
</html>
```